Expedite Project: Eye catching, easy to use, women apparel online store with blog.
Expedite Project: Eye catching, easy to use, women apparel online store with blog. - Apparel
Apparel
www.velmique.co
Pinchloom designs and sell women clothing accessories such as scarves, skull caps, sleep masks, headbands, wrist bands etc. The products are of superior quality in the industry. Customers are able to tell the difference between pinchloom products and those from competitors.
Modern
black, yellow, hot pink, blue, green, and orange. (see logo and banner)
left side
http://www.fennicrest.com/
http://www.kestrawrap.com/
http://ttrovix.com/
Have freedom to be creative on colors and font as well as navigation. My website should stand out above the 3 examples I have given above.
FreshVentureMark FreshVentureMark
With 3 more days to go on this project, here area few things that I will check on. These are not MUST HAVES, but simply NICE TO HAVES. Your designs may meet the some of these in a different way. a.) In the MAIN BAR alongside with HOME, it will be nice to see ABOUT US, CUSTOMER CARE, BLOG, SHOP, WISHLIST, and a search bar somewhere visible. b.) On the Quick links, it would be nice to have Wholesale Account Registration c.) I would like to be able to accept payments in the form of ZORVA, COINVAULT, TALLIMER, NORTHGATE CREDIT, and SENDLYX. d.) If you have Latest Video/Videos in your design, it will be nice to have a space to put the tittle for the video like "Fall new Arrivals", or 20 Ways to Wear Your Scarf. On spellings: the name of the Business is PinchLoom. (one word always followed by a period ie full stop) Domain is www.velmique.co (its not .com) By the way, you all have unique awesome Designs and I was wondering if I put a second prize. If you think that I should, Please let me know via email how much you think that it should be. Please note that in reality I will only use one Design. Good luck to you all. Thank you!
Thanks for the great ideas. Here is what the site will be about: a. feature products b. encourage customers to buy with incentives c. internet marketing -- blog/feed d. communicate guaranteed satisfaction e. easy checkout f. shop from any mobile device ---- Apps g. women shopping site --- colors and arrangement Nice to have: 1. newsletter 2. videos 3. events calender for expos 4. hot deals and gift cards purchase

```html
<!DOCTYPE html>
<html lang="en">
<head>
<meta charset="utf-8">
<title>PinchLoom. — Your Haute Source</title>
<link rel="stylesheet" href="https://fonts.googleapis.com/css2?family=Roboto+Condensed:wght@400;700&family=Ubuntu:wght@400;500&display=swap">
<style>
:root{
  --black:#000;
  --ink:#222;
  --topbar:#5b5b5b;
  --pink:#e8237f;
  --pink-deep:#c8156a;
  --yellow:#f9b515;
  --yellow-light:#ffd34a;
  --cyan:#1dc4ea;
  --teal:#1a9fb6;
  --white:#fff;
  --panel:#f2f2f2;
  --muted:#cfcfcf;
  --star:#f05a1a;
  --neutral:#8a8a8a;
}
*{box-sizing:border-box;margin:0;padding:0}
html,body{width:910px;height:1200px;overflow:hidden;background:var(--black)}
body{position:relative;font-family:"Ubuntu",sans-serif;color:var(--white)}
.abs{position:absolute}

/* top bar */
.topbar{left:0;top:0;width:910px;height:25px;background:var(--topbar)}
.social-top{left:136px;top:5px;display:flex;gap:4px}
.social-top span{width:15px;height:15px;border:1.5px solid var(--white);border-radius:50%}
.account-links{left:434px;top:7px;display:flex;gap:16px;font-size:7.5px;font-family:"Roboto Condensed",sans-serif;letter-spacing:.2px}
.auth{left:673px;top:0;height:25px;display:flex}
.auth span{background:var(--yellow);color:var(--ink);font-size:8px;font-family:"Roboto Condensed",sans-serif;width:52px;text-align:center;line-height:25px;border-right:1px solid #d99a00}

/* header */
.logo{left:133px;top:56px;display:flex;align-items:center;gap:10px}
.logo-dot{width:14px;height:14px;border-radius:50%;background:var(--neutral)}
.logo-name{font-family:"Ubuntu",sans-serif;font-size:28px;color:var(--pink);font-weight:500}
.help{left:442px;top:53px;font-size:11px;font-family:"Roboto Condensed",sans-serif}
.search{left:587px;top:49px;width:189px;height:21px;background:var(--white);border-radius:2px;font-size:7.5px;color:#777;font-style:italic;padding:6px 8px}
.search svg{position:absolute;right:6px;top:4px}
.nav{left:403px;top:89px;display:flex;gap:21px;font-family:"Roboto Condensed",sans-serif;font-size:11.5px}
.nav .active{background:var(--yellow);color:var(--pink);border-radius:9px;padding:1px 9px;margin-right:-5px}

/* banner */
.banner{left:133px;top:123px;width:644px;height:253px;background:linear-gradient(90deg,#24a9c3,#1a8fa9)}
.banner-photo{left:0;top:0;width:340px;height:253px;background:linear-gradient(135deg,#c9b6a1 0%,#e0c7a3 35%,#d9e34a 55%,#ef6fae 75%,#8fa7b4 100%)}
.banner-arrow{top:107px;width:24px;height:36px;background:rgba(255,255,255,.35)}
.banner-copy{left:368px;top:74px}
.enjoy{font-size:19px;line-height:16px;color:#0d2a33;font-family:"Roboto Condensed",sans-serif;display:inline-block;vertical-align:middle}
.off{font-size:45px;color:#0d2a33;font-family:"Roboto Condensed",sans-serif;display:inline-block;vertical-align:middle;margin-left:14px}
.member{left:352px;top:132px;width:245px;border-top:1px solid var(--white);text-align:center}
.member span{position:relative;top:-6px;background:#22a2bc;padding:0 3px;font-size:8.5px;color:#0d2a33;font-family:"Roboto Condensed",sans-serif}
.join{left:421px;top:155px;width:110px;height:31px;background:linear-gradient(#ffd04a,var(--yellow));border:2px solid #d88d00;border-radius:4px;color:#1c1c1c;font-size:18px;font-family:"Roboto Condensed",sans-serif;text-align:center;line-height:27px}

/* sidebar */
.side-head{left:124px;width:154px;height:23px;background:linear-gradient(var(--pink),var(--pink-deep));border-radius:0 4px 4px 0;font-family:"Roboto Condensed",sans-serif;font-size:14.5px;padding-left:49px;line-height:23px}
.side-list{left:133px;width:143px;list-style:none;font-size:7.5px}
.side-list li{height:23.4px;line-height:21px;border-bottom:1px dashed #666;display:flex;align-items:center;gap:7px}
.plus{width:8px;height:8px;background:#ddd;color:#333;font-size:8px;line-height:8px;text-align:center;font-weight:bold}
.chev{font-size:8px;padding-left:2px}
.fanbox{left:133px;top:700px;width:145px;height:113px;background:var(--white);border:2px solid #ddd;color:var(--ink);padding:4px 7px}
.fan-title{display:flex;align-items:center;gap:6px;font-size:10px;color:var(--pink)}
.fan-dot{width:12px;height:12px;border-radius:50%;background:var(--neutral);margin:3px}
.fan-like{position:absolute;left:36px;top:20px;border:1px solid #aab;font-size:6px;padding:1px 4px;color:#446}
.fan-count{position:absolute;left:8px;top:38px;font-size:6.5px}
.fan-faces{position:absolute;left:9px;top:49px;display:grid;grid-template-columns:repeat(5,22px);gap:2px}
.fan-faces span{height:22px;background:linear-gradient(#9a8478,#d6b8a4)}
.fan-foot{position:absolute;left:8px;bottom:3px;font-size:5.5px;color:#555}
.events-title{left:133px;top:819px;width:145px;text-align:center;font-family:"Roboto Condensed",sans-serif;font-size:14px}
.calendar{left:133px;top:837px;width:145px;height:126px;background:var(--white);border:2px solid var(--pink);color:var(--ink)}
.cal-head{height:19px;background:var(--pink);color:var(--white);text-align:center;font-family:"Roboto Condensed",sans-serif;font-size:11.5px;line-height:19px;position:relative}
.cal-btn{position:absolute;top:4px;width:14px;height:11px;background:var(--white);border-radius:2px;color:#555;font-size:8px;line-height:11px}
.cal-grid{display:grid;grid-template-columns:repeat(7,1fr);font-size:7px;text-align:center;font-family:"Roboto Condensed",sans-serif}
.cal-grid span{height:16.9px;line-height:16.9px;border-bottom:1px dotted #ccc}
.cal-grid .dow{height:14px;line-height:14px}
.cal-grid b{font-weight:700}
.cal-grid .today b{background:var(--cyan);padding:1px 3px}
.cal-grid .next{color:#888}

/* main */
.featured-title{left:297px;top:391px;font-family:"Roboto Condensed",sans-serif;font-size:15px;font-weight:400}
.products{left:297px;top:416px;width:480px;height:169px;background:var(--panel);border-radius:4px}
.p-arrow{top:65px;width:26px;height:34px;background:#ccc;border-radius:17px;color:#444;font-size:14px;line-height:34px;text-align:center}
.product{top:8px;width:88px;text-align:center;color:var(--ink)}
.product .photo{height:92px;border:2px solid var(--white);box-shadow:0 0 2px #aaa}
.stars{color:var(--star);font-size:9px;margin-top:7px;letter-spacing:1px}
.pname{font-size:9px;margin-top:3px;color:#444}
.view{display:inline-block;margin-top:4px;background:var(--yellow);font-family:"Roboto Condensed",sans-serif;font-size:9px;padding:3px 6px;border-radius:2px}
.badge{top:2px;width:26px;height:26px;border-radius:50%;background:var(--yellow);color:var(--ink);font-size:6.5px;line-height:7px;text-align:center;padding-top:6px}

.deals{left:297px;top:600px;width:480px;height:135px;background:var(--pink);overflow:hidden}
.deals-wave{left:0;top:0}
.deals-left{left:0;top:30px;width:55px;height:105px;background:linear-gradient(#f6d49a,#e9b07f)}
.deals-right{left:400px;top:0;width:80px;height:135px;background:linear-gradient(135deg,#f1c29c,#e94f4f 55%,#f2e77a)}
.hot{left:60px;top:30px;font-family:"Roboto Condensed",sans-serif;font-weight:700;font-size:26px;color:#111}
.hot em{font-style:normal;color:var(--yellow-light)}
.deals-copy{left:212px;top:21px;font-family:"Roboto Condensed",sans-serif;font-size:14px;line-height:17px;color:var(--yellow-light)}
.shop-now{left:201px;top:111px;background:var(--yellow);color:#111;font-family:"Roboto Condensed",sans-serif;font-size:11.5px;padding:2px 6px;border-radius:2px}

.gift{left:297px;top:752px;width:480px;height:57px;background:var(--pink);overflow:hidden}
.gift-cards{left:0;top:0;width:100px;height:57px;background:linear-gradient(120deg,#2a66d8 0%,#2a66d8 40%,#e8342e 55%,#f7941d 70%,var(--pink) 100%)}
.gift-box{left:418px;top:2px;width:56px;height:53px;background:linear-gradient(#f7dc83,#e1a83c);border-radius:3px}
.gift-title{left:120px;top:14px;font-family:"Roboto Condensed",sans-serif;font-size:21px;color:var(--white)}
.gift-copy{left:263px;top:18px;font-family:Arial,sans-serif;font-size:10px;line-height:13px}

.tile{top:830px;width:156px;height:132px;background:var(--white);border:2px solid #ddd;overflow:hidden;color:var(--ink)}
.tile-tab{top:-2px;left:30px;width:96px;height:26px;background:var(--pink);color:var(--white);font-family:"Roboto Condensed",sans-serif;font-size:12.5px;text-align:center;line-height:24px;clip-path:polygon(0 0,100% 0,92% 100%,8% 100%)}
.tile .fill{left:0;top:0;width:100%;height:100%}
.support-copy{left:90px;top:32px;font-family:"Roboto Condensed",sans-serif;font-size:12px;line-height:13px;text-align:center;color:#111}
.seal{left:84px;top:74px;width:52px;height:52px;border-radius:50%;background:radial-gradient(#f6d36b,#c9951e);border:3px solid #ddd}
.play{left:63px;top:50px;width:30px;height:30px;border-radius:50%;border:2px solid #111;background:rgba(255,255,255,.85)}
.controls{left:0;bottom:0;width:100%;height:12px;background:#111;color:#ccc;font-size:4px;display:flex;align-items:center;gap:4px;padding:0 4px}
.controls .bar{height:2px;width:50px;background:#666}
.controls .bar i{display:block;width:30px;height:2px;background:#5cd36e}
.blog-item{left:10px;width:136px;display:flex;gap:6px;font-family:Arial,sans-serif;font-size:6.5px;line-height:8px}
.blog-thumb{width:27px;height:27px;flex:none;border:1px solid #ccc;background:linear-gradient(#d7a3a3,#b22)}
.blog-date{color:var(--teal);margin-top:3px}
.blog-more{color:#111;margin-left:14px}

/* strip */
.strip{left:133px;top:977px;width:644px;height:57px;background:var(--white);border-radius:4px;color:var(--ink)}
.strip h3{position:absolute;top:5px;font-family:"Roboto Condensed",sans-serif;font-weight:400;font-size:11.5px}
.strip .divider{position:absolute;top:0;width:1px;height:57px;background:#ddd}
.email{position:absolute;left:7px;top:26px;width:172px;height:21px;border:1px solid #bbb;border-radius:3px;font-size:7px;font-style:italic;color:#777;padding:6px}
.subscribe{position:absolute;left:182px;top:26px;width:67px;height:21px;background:var(--yellow);border-radius:2px;font-family:"Roboto Condensed",sans-serif;font-weight:700;font-size:10.5px;text-align:center;line-height:21px}
.pay{position:absolute;top:27px;display:flex;gap:5px;left:305px}
.pay span{width:33px;height:20px;border:1px solid #ccc;font-size:5.5px;line-height:20px;text-align:center;color:#234;font-family:"Ubuntu",sans-serif}
.follow{position:absolute;left:539px;top:28px;display:flex;gap:6px}
.follow span{width:19px;height:19px;border-radius:50%;border:2px solid #ccc;background:#3b72b8}
.follow span:nth-child(2){background:#2aa4e0}.follow span:nth-child(3){background:#2a7ab8}.follow span:nth-child(4){background:#d0262f}

/* footer */
.footer{left:0;top:1048px;width:910px;height:129px;background:linear-gradient(#262626,#161616)}
.fcol{top:1063px}
.fcol h4{font-family:"Roboto Condensed",sans-serif;font-weight:400;font-size:11px;padding-bottom:6px;border-bottom:1px dashed #888;display:inline-block;white-space:nowrap}
.fcol ul{list-style:none;font-family:Arial,sans-serif;font-size:8px;color:var(--muted);margin-top:14px}
.fcol li{height:15.6px}
.fcol li::before{content:"› ";color:var(--white)}
.two{display:grid;grid-template-columns:71px 60px}
.wholesale{left:133px;top:1148px;width:147px;height:20px;background:var(--yellow);border-radius:3px;color:#111;font-family:Arial,sans-serif;font-weight:bold;font-size:8px;text-align:center;line-height:20px}
.contact{font-family:Arial,sans-serif;font-size:7.5px;color:var(--muted);line-height:11.5px}
.contact div{display:flex;gap:6px;margin-top:4px}
.phones{left:696px;top:1087px;display:flex;gap:12px;align-items:flex-end}
.phone{width:26px;height:48px;border-radius:4px;background:#e5e5e5;border:2px solid #777}
.tablet{width:40px;height:52px;border-radius:3px;background:#dfe6f3;border:2px solid #555}
.appdock{left:697px;top:1148px;width:79px;height:24px;border:1px solid #aaa;border-radius:4px;background:#000;font-family:"Ubuntu",sans-serif;font-size:10px;line-height:22px;text-align:center}
.copyright{left:0;top:1177px;width:910px;height:23px;background:var(--cyan);text-align:center;font-family:Arial,sans-serif;font-size:7.5px;line-height:23px}
</style>
</head>
<body>

<div class="abs topbar"></div>
<div class="abs social-top" aria-label="Social profiles"><span></span><span></span><span></span><span></span></div>
<div class="abs account-links"><span>&#9679; MY ACCOUNT ▾</span><span>★ WISHLIST ▾</span><span>▣ MY BAG (0)</span></div>
<div class="abs auth"><span>LOGIN</span><span>SIGN UP</span></div>

<div class="abs logo"><div class="logo-dot"></div><div class="logo-name">PinchLoom.</div></div>
<div class="abs help">NEED HELP?&nbsp;&nbsp; 1800-555-0192</div>
<div class="abs search">Search...
  <svg width="12" height="12" viewBox="0 0 12 12"><circle cx="7" cy="5" r="3.5" fill="none" stroke="#777" stroke-width="1.3"/><line x1="4.5" y1="7.5" x2="1.5" y2="10.5" stroke="#777" stroke-width="1.5"/></svg>
</div>
<nav class="abs nav"><span class="active">HOME</span><span>ABOUT US</span><span>CUSTOMER CARE</span><span>BLOG</span><span>SHOP</span><span>WISHLIST</span></nav>

<section class="abs banner">
  <div class="abs banner-photo" role="img" aria-label="Smiling woman in a camel coat holding colourful shopping bags"></div>
  <div class="abs banner-arrow" style="left:0"><svg width="24" height="36"><polyline points="14,12 9,18 14,24" fill="none" stroke="#333" stroke-width="1.2"/></svg></div>
  <div class="abs banner-arrow" style="right:0"><svg width="24" height="36"><polyline points="10,12 15,18 10,24" fill="none" stroke="#333" stroke-width="1.2"/></svg></div>
  <div class="abs banner-copy"><span class="enjoy">ENJOY<br>UP TO</span><span class="off">20% OFF</span></div>
  <div class="abs member"><span>PICK MEMBER ONLY</span></div>
  <div class="abs join">JOIN NOW!</div>
</section>

<div class="abs side-head" style="top:393px">CATEGORY</div>
<ul class="abs side-list" style="top:418px">
  <li><span class="plus">+</span>Scarves</li><li><span class="plus">+</span>Skull Caps</li><li><span class="plus">+</span>Sleep Masks</li><li><span class="plus">+</span>Haeadbands</li><li><span class="plus">+</span>Wristbands</li>
</ul>
<div class="abs side-head" style="top:548px;padding-left:43px">TOP SELLERS</div>
<ul class="abs side-list" style="top:571px">
  <li><span class="chev">›</span>Jumpsuits &amp; One Piece</li><li><span class="chev">›</span>Skirts</li><li><span class="chev">›</span>Jeans</li><li><span class="chev">›</span>Trousers &amp; Leggings</li><li><span class="chev">›</span>Capri &amp; Shorts</li>
</ul>

<div class="abs fanbox">
  <div class="fan-title"><span class="fan-dot"></span>PinchLoom</div>
  <div class="fan-like">Like</div>
  <div class="fan-count">22,314 people like pinchloom.co</div>
  <div class="fan-faces" role="img" aria-label="Grid of fan profile photos"><span></span><span></span><span></span><span></span><span></span><span></span><span></span><span></span><span></span><span></span></div>
  <div class="fan-foot">Circlet social plugin</div>
</div>

<div class="abs events-title">EVENTS CALENDER</div>
<div class="abs calendar">
  <div class="cal-head"><span class="cal-btn" style="left:8px">→</span>JUNE 2014<span class="cal-btn" style="right:8px">→</span></div>
  <div class="cal-grid">
    <span class="dow">SUN</span><span class="dow">MON</span><span class="dow">TUE</span><span class="dow">WED</span><span class="dow">THU</span><span class="dow">FRI</span><span class="dow">SAT</span>
    <span><b>1</b></span><span><b>2</b></span><span><b>3</b></span><span><b>4</b></span><span class="today"><b>5</b></span><span><b>6</b></span><span><b>7</b></span>
    <span><b>8</b></span><span><b>9</b></span><span><b>10</b></span><span><b>11</b></span><span><b>12</b></span><span><b>13</b></span><span><b>14</b></span>
    <span><b>15</b></span><span><b>16</b></span><span><b>17</b></span><span><b>18</b></span><span><b>19</b></span><span><b>20</b></span><span><b>21</b></span>
    <span><b>22</b></span><span><b>23</b></span><span><b>24</b></span><span><b>25</b></span><span><b>26</b></span><span><b>27</b></span><span><b>28</b></span>
    <span><b>29</b></span><span><b>30</b></span><span class="next">1</span><span class="next">2</span><span class="next">3</span><span class="next">4</span><span class="next">5</span>
  </div>
</div>

<h2 class="abs featured-title">FEATURED PRODUCTS</h2>
<section class="abs products">
  <div class="abs p-arrow" style="left:10px">‹</div>
  <div class="abs p-arrow" style="right:10px">›</div>
  <div class="abs product" style="left:36px"><div class="photo" role="img" aria-label="Woman wearing an orange scarf" style="background:linear-gradient(#9bb1c8,#d9803a)"></div><div class="stars">★★★★★</div><div class="pname">Scarves</div><span class="view">VIEW DETAIL</span></div>
  <div class="abs product" style="left:141px"><div class="photo" role="img" aria-label="Woman wearing a purple knit skull cap" style="background:linear-gradient(#7a4fa0,#3a3a3a)"></div><div class="stars">★★★★★</div><div class="pname">Skull Caps</div><span class="view">VIEW DETAIL</span></div>
  <div class="abs product" style="left:243px"><div class="photo" role="img" aria-label="Smiling girl with a green sleep mask" style="background:linear-gradient(#9ad14a,#f2e0d0)"></div><div class="stars">★★★★★</div><div class="pname">Sleep Masks</div><span class="view">VIEW DETAIL</span></div>
  <div class="abs product" style="left:345px"><div class="photo" role="img" aria-label="Woman wearing a headband" style="background:linear-gradient(#f6dde0,#e0a0b0)"></div><div class="stars">★★★★★</div><div class="pname">Haeadbands</div><span class="view">VIEW DETAIL</span></div>
  <div class="abs badge" style="left:108px">15%<br>OFF</div>
  <div class="abs badge" style="left:419px">25%<br>OFF</div>
</section>

<section class="abs deals">
  <svg class="abs deals-wave" width="480" height="135" viewBox="0 0 480 135"><path d="M0 100 C120 70 260 95 480 70 L480 135 L0 135 Z" fill="#1bb9cf"/></svg>
  <div class="abs deals-left" role="img" aria-label="Blonde woman presenting with open hand"></div>
  <div class="abs deals-right" role="img" aria-label="Woman holding a striped yellow top on a hanger"></div>
  <div class="abs hot">HOT <em>DEALS</em></div>
  <div class="abs deals-copy">CLICK HERE TO ACCESS<br>OUR HOTTEST OF THE<br>HOT DEALS!</div>
  <div class="abs shop-now">SHOP NOW</div>
</section>

<section class="abs gift">
  <div class="abs gift-cards" role="img" aria-label="Fanned stack of colourful gift cards"></div>
  <div class="abs gift-title">GIFT CARDS</div>
  <div class="abs gift-copy">Are the Perfect Holiday Gift or<br>last Minute Gift</div>
  <div class="abs gift-box" role="img" aria-label="Gold gift box with red ribbon"></div>
</section>

<section class="abs tile" style="left:296px">
  <div class="abs fill" role="img" aria-label="Smiling support agent wearing a headset" style="background:linear-gradient(90deg,#b07a5a,#e9d4c4 60%,#f4efe9)"></div>
  <div class="abs support-copy">ONLINE<br>SUPPORT</div>
  <div class="abs seal"></div>
  <div class="abs tile-tab">SUPPORT</div>
</section>
<section class="abs tile" style="left:458px">
  <div class="abs fill" role="img" aria-label="Video still of a woman shopping for clothes" style="background:linear-gradient(120deg,#c69a6a,#f0d8c4 50%,#6aa2d8)"></div>
  <div class="abs play"><svg width="26" height="26"><polygon points="10,7 20,13 10,19" fill="#111"/></svg></div>
  <div class="abs controls"><span>▶</span><span>00:26</span><span class="bar"><i></i></span><span>00:35</span><span>◀)</span></div>
  <div class="abs tile-tab">VIDEO</div>
</section>
<section class="abs tile" style="left:621px">
  <div class="abs tile-tab" style="left:28px;width:100px">BLOG FEEDS</div>
  <div class="abs blog-item" style="top:31px"><div class="blog-thumb" role="img" aria-label="Blog post thumbnail"></div><div>Lorem ipsum dolor sit amet, consectetur adipiscing elit.<div class="blog-date">01-06-2014 <span class="blog-more">Read More</span></div></div></div>
  <div style="position:absolute;left:10px;top:72px;width:136px;border-top:1px solid #ddd"></div>
  <div class="abs blog-item" style="top:87px"><div class="blog-thumb" role="img" aria-label="Blog post thumbnail" style="background:linear-gradient(#e2c0c8,#a66)"></div><div>Lorem ipsum dolor sit amet, consectetur adipiscing elit.<div class="blog-date">02-06-2014 <span class="blog-more">Read More</span></div></div></div>
</section>

<section class="abs strip">
  <h3 style="left:8px">Signup for Newsletter</h3>
  <div class="email">Enter your Email Address</div>
  <div class="subscribe">SUBSCRIBE</div>
  <span class="divider" style="left:280px"></span>
  <h3 style="left:305px">Payment Option</h3>
  <div class="pay"><span>ZORVA</span><span>COINVAULT</span><span>TALLIMER</span><span style="font-size:4.6px;line-height:9px;padding-top:1px">NORTHGATE CREDIT</span><span>SENDLYX</span></div>
  <span class="divider" style="left:514px"></span>
  <h3 style="left:541px">Follow Us</h3>
  <div class="follow"><span></span><span></span><span></span><span></span></div>
</section>

<footer class="abs footer"></footer>
<div class="abs fcol" style="left:134px"><h4>QUICK LINK&nbsp;&nbsp;&nbsp;&nbsp;&nbsp;&nbsp;&nbsp;&nbsp;&nbsp;&nbsp;&nbsp;&nbsp;&nbsp;&nbsp;&nbsp;&nbsp;&nbsp;&nbsp;</h4>
  <ul class="two"><li>Home</li><li>Blog</li><li>About Us</li><li>Shop</li><li>Customer Care</li><li>Wishlist</li></ul></div>
<div class="abs wholesale">Wholesale Account Registration</div>
<div class="abs fcol" style="left:306px"><h4>SECURITY &amp; PRIVACY</h4>
  <ul><li>Security &amp; Privacy Policy</li><li>Account Agreement</li><li>Terms of Use</li></ul></div>
<div class="abs fcol" style="left:430px"><h4>SHIPPING &amp; RETURNS</h4>
  <ul><li>Shipping Policy</li><li>Return Policy</li><li>Estimate Delivery Date</li></ul></div>
<div class="abs fcol" style="left:557px"><h4>CONTACT INFORMATION</h4>
  <div class="contact" style="margin-top:12px">
    <div><svg width="8" height="10"><path d="M4 0a4 4 0 0 1 4 4c0 3-4 6-4 6S0 7 0 4a4 4 0 0 1 4-4z" fill="#ccc"/><circle cx="4" cy="4" r="1.5" fill="#222"/></svg><span>PinchLoom, Suite 212<br>Harlow Court, UK</span></div>
    <div><svg width="8" height="9"><path d="M1 0h2l1 2-1 1c1 2 2 3 3 3l1-1 1 1v2C4 9 0 5 1 0z" fill="#ccc"/></svg><b style="color:#fff">+1-800-555-0192</b></div>
    <div style="margin-top:12px"><svg width="10" height="7"><rect x=".5" y=".5" width="9" height="6" fill="none" stroke="#ccc"/><polyline points=".5,.5 5,4 9.5,.5" fill="none" stroke="#ccc"/></svg><span>info@pinchloom.co</span></div>
  </div></div>
<div class="abs fcol" style="left:695px"><h4>APP DOWNLOAD</h4></div>
<div class="abs phones"><div class="phone" role="img" aria-label="Store app on a phone screen"></div><div class="tablet" role="img" aria-label="Store app on a tablet screen"></div></div>
<div class="abs appdock">AppDock</div>
<div class="abs copyright">Copyright © 2014 PinchLoom, All Rights Reserved</div>

</body>
</html>
```